Letterhead for SaaS

Design a letterhead that aligns with our new business card, using our logo and color scheme and text defined in the Branding Guide to ensure consistency. Consider incorporating a subtle watermark for added elegance. The layout should reflect the card's style, creating a cohesive look across our stationery.

```html
<!DOCTYPE html>
<html lang="en">
<head>
<meta charset="utf-8">
<title>Vardell Letterhead</title>
<link rel="stylesheet" href="https://fonts.googleapis.com/css2?family=Montserrat:wght@400;500;700;800&display=swap">
<style>
  :root {
    --backdrop: #e4e4e4;
    --paper: #f5f5f5;
    --ink-navy: #131a2b;
    --accent-blue: #3dbbe6;
    --header-text: #ffffff;
    --watermark: #e6e6e9;
    --gap-white: #f8f8f8;
  }
  html, body {
    margin: 0;
    padding: 0;
    width: 1153px;
    height: 1200px;
    overflow: hidden;
    background: var(--backdrop);
  }
  .canvas {
    position: relative;
    width: 1153px;
    height: 1200px;
  }
  .letterhead {
    position: absolute;
    left: 166px;
    top: 26px;
    width: 820px;
    height: 1148px;
    background: var(--paper);
    box-shadow: 0 6px 24px rgba(0,0,0,0.18);
  }
  .letterhead svg {
    display: block;
    width: 100%;
    height: 100%;
  }
  .sheet-text {
    font-family: "Montserrat", sans-serif;
  }
  .contact-name { font-weight: 700; font-size: 19px; fill: var(--header-text); }
  .contact-role { font-weight: 400; font-size: 18px; fill: var(--header-text); }
  .contact-line { font-weight: 400; font-size: 17px; fill: var(--header-text); }
  .brand-name { font-weight: 800; font-size: 36px; fill: var(--ink-navy); letter-spacing: 1px; }
  .watermark-name { font-weight: 800; font-size: 150px; fill: var(--watermark); letter-spacing: 6px; }
  .footer-web { font-weight: 400; font-size: 22px; fill: var(--header-text); letter-spacing: 0.5px; }
</style>
</head>
<body>
<main class="canvas">
  <article class="letterhead">
    <svg viewBox="0 0 1069 1496" xmlns="http://www.w3.org/2000/svg" class="sheet-text">
      <defs>
        <linearGradient id="header-shade" x1="0" y1="0" x2="1" y2="1">
          <stop offset="0" stop-color="#0f1524"/>
          <stop offset="0.55" stop-color="#19213a"/>
          <stop offset="1" stop-color="#0e1322"/>
        </linearGradient>
      </defs>

      <!-- header band -->
      <g class="header-wave">
        <path fill="url(#header-shade)" d="M0,0 H1069 V250 C900,256 760,215 620,170 C430,100 220,55 0,82 Z"/>
        <path fill="var(--accent-blue)" d="M0,96 C200,62 380,80 502,145 C380,112 200,98 0,150 Z"/>
        <path fill="var(--accent-blue)" d="M620,188 C770,240 910,262 1069,257 V292 C900,295 760,252 620,188 Z"/>
      </g>

      <!-- contact block -->
      <g class="contact-block">
        <text class="contact-name" x="755" y="77">Marcus D. Hale</text>
        <text class="contact-role" x="755" y="100">Founder + CEO</text>
        <g class="icon-phone" fill="#ffffff">
          <path d="M756,118 h12 a2,2 0 0 1 2,2 v2 h-4 v-1 h-8 v1 h-4 v-2 a2,2 0 0 1 2,-2 z"/>
          <rect x="757" y="123" width="10" height="6" rx="1"/>
        </g>
        <text class="contact-line" x="780" y="130">(555) 014-2297</text>
        <g class="icon-mail">
          <rect x="755" y="146" width="14" height="9" fill="#ffffff"/>
          <path d="M755,146 L762,152 L769,146" fill="none" stroke="#131a2b" stroke-width="1.3"/>
        </g>
        <text class="contact-line" x="780" y="154">marcus.h@vardell.com</text>
        <g class="icon-globe" fill="none" stroke="#ffffff" stroke-width="1.4">
          <circle cx="762" cy="173" r="6.5"/>
          <ellipse cx="762" cy="173" rx="2.8" ry="6.5"/>
          <line x1="755.5" y1="173" x2="768.5" y2="173"/>
        </g>
        <text class="contact-line" x="780" y="177">www.vardell.com</text>
      </g>

      <!-- brand name -->
      <g class="brand-block">
        <circle cx="195" cy="230" r="26" fill="var(--ink-navy)"/>
        <text class="brand-name" x="200" y="372" text-anchor="middle">VARDELL</text>
      </g>

      <!-- watermark -->
      <text class="watermark-name" x="534" y="800" text-anchor="middle">VARDELL</text>

      <!-- footer -->
      <g class="footer-band">
        <path fill="var(--ink-navy)" d="M0,1441 H612 L601,1452 H0 Z"/>
        <path fill="var(--accent-blue)" d="M0,1462 H592 L562,1496 H0 Z"/>
        <path fill="var(--ink-navy)" d="M636,1425 H1069 V1496 H570 Z"/>
        <text class="footer-web" x="820" y="1469" text-anchor="middle">www.vardellstudio.com</text>
      </g>
    </svg>
  </article>
</main>
</body>
</html>
```